Brochure Design

We need a 6 page Brochure designed for our product, please see attached document for more information. The content should focus on account work.

Target Market(s)

Businesses that use a taxi service for their business

Requirements
Must have
• Must have key content on the services we provide for Account work

```html
<!DOCTYPE html>
<html lang="en">
<head>
<meta charset="utf-8">
<title>Tavo Account Services Brochure</title>
<link href="https://fonts.googleapis.com/css2?family=Bebas+Neue&family=Open+Sans:ital,wght@0,400;0,700;1,700;1,800&family=Roboto+Condensed:wght@700&display=swap" rel="stylesheet">
<style>
  :root {
    --kraft: #c4996b;
    --label: #ffffff;
    --paper: #f1f1ef;
    --yellow: #fbc00c;
    --ink: #2b2b2b;
    --grey-text: #4a4a4a;
    --dark: #262626;
    --white: #ffffff;
    --divider: rgba(43,43,43,0.25);
  }
  * { box-sizing: border-box; margin: 0; padding: 0; }
  html, body { width: 1200px; height: 462px; overflow: hidden; }
  body { background: var(--kraft); position: relative; font-family: "Open Sans", sans-serif; color: var(--ink); }

  .panel-label {
    position: absolute; top: 18px; font: italic 800 15px "Open Sans", sans-serif;
    color: var(--label); letter-spacing: 0.5px;
  }
  .fold-line { position: absolute; top: 34px; bottom: 0; border-left: 1px dashed rgba(60,40,20,0.55); }

  .sheet { position: absolute; left: 46px; top: 45px; width: 1122px; height: 372px; box-shadow: 2px 3px 6px rgba(0,0,0,0.3); overflow: hidden; }

  /* Inside flap — features */
  .features { position: absolute; left: 0; top: 0; width: 198px; height: 372px; background: var(--paper); text-align: center; }
  .feature { position: absolute; left: 0; width: 198px; }
  .feature svg { display: block; margin: 0 auto; }
  .feature h3 { font-weight: 400; font-size: 10px; letter-spacing: 0.2px; margin-top: 6px; color: var(--grey-text); }
  .feature p { font-size: 7px; line-height: 10px; margin: 6px auto 0; width: 150px; color: var(--grey-text); }

  /* Inside flap — by-lines */
  .bylines { position: absolute; left: 198px; top: 0; width: 125px; height: 372px; background: var(--yellow); text-align: center; }
  .brand-mark { display: flex; align-items: center; justify-content: center; gap: 4px; font-weight: 700; color: var(--dark); }
  .brand-mark .dot { border-radius: 50%; background: var(--dark); }
  .bylines .brand-mark { margin-top: 24px; font-size: 26px; }
  .bylines .brand-mark .dot { width: 18px; height: 18px; }
  .bylines h2 { font: 400 17px/16px "Bebas Neue", sans-serif; margin-top: 18px; color: var(--dark); }
  .bylines ul { list-style: none; margin: 10px 10px 0; border-top: 1px solid var(--divider); }
  .bylines li { font-size: 6.8px; font-weight: 700; line-height: 9px; padding: 5px 0; border-bottom: 1px solid var(--divider); text-transform: uppercase; }
  .bylines li:last-child { border-bottom: none; }

  /* Back panel */
  .back { position: absolute; left: 323px; top: 0; width: 423px; height: 372px; }
  .back .photo { position: absolute; inset: 0; background: linear-gradient(100deg, #d9d4cf 0%, #b9a592 28%, #cfc9c2 55%, #e6e3df 100%); }
  .back .brand-mark { position: absolute; left: 92px; top: 54px; font-size: 28px; }
  .back .brand-mark .dot { width: 20px; height: 20px; }
  .phone { position: absolute; background: #1d1d1d; border-radius: 14px; }
  .phone .screen { position: absolute; left: 5px; right: 5px; top: 22px; bottom: 24px; background: linear-gradient(#fbc00c 0 10%, #e9e6dc 10% 75%, #ffffff 75%); }
  .back .headline { position: absolute; left: 243px; top: 243px; font: 400 34px/30px "Bebas Neue", sans-serif; color: var(--white); }
  .contact { position: absolute; right: 14px; top: 313px; text-align: right; font-size: 7.5px; font-weight: 700; line-height: 12px; color: var(--dark); }
  .contact .email { margin-bottom: 7px; letter-spacing: 0.6px; }

  /* Front panel */
  .front { position: absolute; left: 746px; top: 0; width: 376px; height: 372px; background: var(--yellow); }
  .front .photo { position: absolute; left: 0; top: 0; width: 376px; height: 300px; background: linear-gradient(120deg, #d8d8d6 0%, #8b8d90 35%, #3a3a3c 70%, #1e1e20 100%); }
  .front .wave { position: absolute; left: 0; top: 236px; }
  .front .brand-mark { position: absolute; left: 84px; top: 56px; font-size: 28px; }
  .front .brand-mark .dot { width: 20px; height: 20px; }
  .front .headline { position: absolute; right: 22px; top: 22px; text-align: right; font: 400 33px/28px "Bebas Neue", sans-serif; color: var(--dark); }
  .front .web { position: absolute; left: 16px; top: 347px; font: italic 700 13px "Open Sans", sans-serif; color: var(--dark); }
  .front .cta { position: absolute; right: 20px; top: 321px; text-align: right; }
  .front .cta strong { display: block; font: 400 20px/20px "Bebas Neue", sans-serif; color: var(--dark); letter-spacing: 0.3px; }
  .front .cta span { display: block; font: 700 12px "Roboto Condensed", sans-serif; color: var(--dark); }
</style>
</head>
<body>
  <div class="panel-label" style="left:142px">INSIDE FLAP</div>
  <div class="panel-label" style="left:563px">BACK</div>
  <div class="panel-label" style="left:960px">FRONT</div>
  <div class="fold-line" style="left:418px"></div>
  <div class="fold-line" style="left:792px"></div>

  <main class="sheet">
    <section class="features">
      <div class="feature" style="top:22px">
        <svg width="28" height="28" viewBox="0 0 28 28"><path d="M6 4c2-1 3 0 4 2l1 4c0 1-1 2-2 3 1 3 3 5 6 6 1-1 2-2 3-2l4 1c2 1 3 2 2 4l-1 2c-1 1-3 2-5 1C11 22 6 17 4 10c-1-2 0-4 2-6z" fill="var(--yellow)"/><path d="M16 6a6 6 0 0 1 6 6M16 2a10 10 0 0 1 10 10" stroke="var(--dark)" stroke-width="2" fill="none" stroke-linecap="round"/></svg>
        <h3>24/7 SUPPORT</h3>
        <p>Our Account Management Team, support 24/7/365 from our HQ in London.</p>
      </div>
      <div class="feature" style="top:136px">
        <svg width="20" height="30" viewBox="0 0 20 30"><path d="M10 2a7 7 0 0 1 7 7c0 5-7 12-7 12S3 14 3 9a7 7 0 0 1 7-7z" fill="var(--yellow)"/><circle cx="10" cy="9" r="2.5" fill="var(--white)"/><ellipse cx="10" cy="24" rx="8" ry="3.5" fill="none" stroke="var(--dark)" stroke-width="2.5"/></svg>
        <h3>AVERAGE 7 MIN PICK UPS</h3>
        <p>Benefit from a priority service, ensuring we're only ever moments away.</p>
      </div>
      <div class="feature" style="top:266px">
        <svg width="40" height="24" viewBox="0 0 40 24"><path d="M4 16l2-6 6-5h14l7 5 4 2v4z" fill="var(--yellow)"/><path d="M13 7h6v4h-8zM21 7h5l4 4h-9z" fill="var(--white)"/><circle cx="11" cy="17" r="4" fill="var(--white)" stroke="var(--dark)" stroke-width="2.5"/><circle cx="30" cy="17" r="4" fill="var(--white)" stroke="var(--dark)" stroke-width="2.5"/></svg>
        <h3>TRAINED, HAND PICKED DRIVERS</h3>
        <p>Our drivers are trained and vetted to ensure high service, quality and safety.</p>
      </div>
    </section>

    <section class="bylines">
      <div class="brand-mark"><span class="dot"></span>tavo</div>
      <h2>Other by-lines that<br>can be used are:</h2>
      <ul>
        <li>Cost effective service with quality vehicles</li>
        <li>Dedicated access via online system</li>
        <li>Bookings can be made quickly and simply</li>
        <li>Phone support when needed, 24x7</li>
        <li>Advanced booking options</li>
        <li>Regular repeat scheduled booking options</li>
        <li>Airport transfers</li>
        <li>Mid-range to executive vehicles</li>
        <li>Your entry point to the UK-wide Tavo network</li>
      </ul>
    </section>

    <section class="back">
      <div class="photo" role="img" aria-label="Photo of a smiling passenger on a phone call in a bright city street"></div>
      <div class="brand-mark"><span class="dot"></span>tavo</div>
      <div class="phone" style="left:277px;top:35px;width:96px;height:178px" role="img" aria-label="Smartphone showing the on-board screen of the booking app"><div class="screen"></div></div>
      <div class="phone" style="left:235px;top:35px;width:100px;height:198px" role="img" aria-label="Smartphone showing a ride request map in the booking app"><div class="screen"></div></div>
      <div class="headline">Your safety is<br>our priority!</div>
      <div class="contact">
        <div class="email">info@tavo.example</div>
        <div>Canada: Tel: +1 (555) 010 2234</div>
        <div>USA: Tel: +1 (555) 013 4471</div>
        <div>Pakistan: Tel: +92 300 0000 123</div>
      </div>
    </section>

    <section class="front">
      <div class="photo" role="img" aria-label="Photo of a driver's hand on a car steering wheel"></div>
      <svg class="wave" width="376" height="136" viewBox="0 0 376 136">
        <path d="M0 60 C90 10 230 -5 376 40 L376 136 L0 136 Z" fill="var(--dark)"/>
        <path d="M0 78 C100 30 240 20 376 58 L376 136 L0 136 Z" fill="var(--yellow)"/>
      </svg>
      <div class="brand-mark"><span class="dot"></span>tavo</div>
      <div class="headline">Your safety is<br>our priority!</div>
      <div class="web">www.tavo.example</div>
      <div class="cta"><strong>Download the Tavo app</strong><span>From your SmartPhone today!</span></div>
    </section>
  </main>
</body>
</html>
```